Butcher shop

We have 2 butcher shops:

Shop 9, Ridgeway Court, Aberdeen NSW 2336
Ph 02 6512 3840

47 Marlow St, Scone NSW 2337
Ph 02 6518 2274

ABN 48 907 215 816

I would like this info on reverse of card and my personal info on front of card. I have a logo I would like to use also. Require a very smooth thick matte card, with colour both sides.

Front of card should say:

Linda Farrugia
Accounts

Ph 0437 620 915
E lindafarrugia@quollmail.com.au

Industry/Entity Type

Shop

Contact Information for Business Card

Linda Farrugia
Ph 0437 620 915

Logo Text

Farrugia's Quality Meats

Logo styles of interest
Pictorial/Combination Logo
Requirements
Must have
• We use Century Gothic Font

```html
<!DOCTYPE html>
<html lang="en">
<head>
<meta charset="utf-8">
<title>Farrugia's Quality Meats – Business Card</title>
<link rel="stylesheet" href="https://fonts.googleapis.com/css2?family=Questrial&display=swap">
<style>
  :root {
    --stage: #2b2b2b;
    --sky: #8fd6f2;
    --navy: #27276e;
    --ink: #0a0a0a;
    --white: #ffffff;
    --card-w: 880px;
    --card-h: 530px;
  }
  * { margin: 0; padding: 0; box-sizing: border-box; }
  html, body {
    width: 1200px; height: 1200px; overflow: hidden;
    background: radial-gradient(circle at 50% 45%, #3a3a3a, var(--stage) 70%);
    font-family: "Questrial", "Century Gothic", sans-serif;
  }
  .stage {
    position: relative; width: 1200px; height: 1200px;
    display: flex; flex-direction: column; align-items: center; justify-content: center; gap: 50px;
  }
  .card {
    position: relative; width: var(--card-w); height: var(--card-h);
    overflow: hidden; box-shadow: 0 18px 40px rgba(0,0,0,.55);
  }

  /* Front */
  .card--front { background: var(--sky); color: var(--ink); }
  .card--front .band-top { position: absolute; top: 0; left: 0; right: 0; height: 30px; background: var(--navy); }
  .card--front .band-bottom { position: absolute; left: 0; right: 0; bottom: 56px; height: 40px; background: var(--navy); }
  .card--front .base { position: absolute; left: 0; right: 0; bottom: 0; height: 56px; background: var(--ink); }
  .card--front .brand {
    position: absolute; left: 60px; top: 200px;
    font-size: 44px; line-height: 1.05; color: var(--ink);
  }
  .card--front .divider {
    position: absolute; left: 430px; top: 140px; width: 2px; height: 190px; background: var(--ink);
  }
  .person { position: absolute; left: 480px; top: 120px; }
  .person .name { font-size: 34px; line-height: 1.1; }
  .person .role { font-size: 32px; line-height: 1.1; padding-left: 30px; }
  .person .contact { margin-top: 34px; padding-left: 60px; font-size: 20px; line-height: 1.4; }

  /* Back */
  .card--back { background: var(--ink); color: var(--white); }
  .card--back .band-bottom { position: absolute; left: 0; right: 0; bottom: 0; height: 52px; background: var(--navy); }
  .card--back .brand {
    position: absolute; left: 240px; top: 130px;
    font-size: 56px; line-height: 1.05; color: var(--sky);
  }
  .card--back .abn { position: absolute; left: 380px; top: 272px; font-size: 24px; }
  .shop { position: absolute; font-size: 24px; line-height: 1.35; font-style: normal; }
  .shop .phone { color: var(--sky); }
  .shop--yarrowvale { left: 60px; top: 350px; }
  .shop--kestrel { left: 640px; top: 180px; }
</style>
</head>
<body>
<main class="stage">
  <section class="card card--front" aria-label="Card front">
    <div class="band-top"></div>
    <p class="brand">Farrugia's<br>Quality Meats</p>
    <div class="divider"></div>
    <div class="person">
      <p class="name">Linda Farrugia</p>
      <p class="role">Accounts</p>
      <p class="contact">Ph 0437 620 915<br>E lindafarrugia@quollmail.com.au</p>
    </div>
    <div class="band-bottom"></div>
    <div class="base"></div>
  </section>

  <section class="card card--back" aria-label="Card back">
    <p class="brand">Farrugia's<br>Quality Meats</p>
    <p class="abn">ABN 48 907 215 816</p>
    <address class="shop shop--kestrel">47 Marlow St,<br>Kestrel Flats NSW 2419<br><span class="phone">Ph 02 6518 2274</span></address>
    <address class="shop shop--yarrowvale">Shop 9, Ridgeway Court,<br>Yarrowvale NSW 2418<br><span class="phone">Ph 02 6512 3840</span></address>
    <div class="band-bottom"></div>
  </section>
</main>
</body>
</html>
```